Pull Up Banner - Recruitment Company

We would like a design for a pull up banner.

For context: we are a recruitment business. We specialise in helping people in healthcare industry to find jobs in Australia.

I have come up with several ideas and text for the banner. Feel free to use the following as you see appropriate:

- Our logo (see attached)
- 'Healthcare Recruitment Agency'
- Some sort of imagine / cartoon of medical professionals (ie. doctor, nurse, physiotherapist, speech pathologist). A cartoon is more friendly than committing to a photo
- 'Empowering your next career move'
- 'Discover tailored opportunities based on your career preferences'
- Dot points (allied health, nursing, medical imaging)
- Contact info at the bottom including our website (www.quellstaffing.com.au, our Instagram handle @quellstaffing, Mobile: XXXX XXX XXX. The title section for contact information could be 'Get in touch:'

Feel free to submit a couple of designs and we can merge aspects that look good on your designs and find the perfect fit.
Thank you
Updates

Hello,

Thank you for your initial submissions to this project. I appreciate the time you've invested.

After reviewing the first attempt, I'd like to share some feedback and initial observations:

- Professionalism and engagement: Is the overall appearance of the banner professional? It's crucial that we have a high-quality design as this will represent our business.

- Image selection: The image (whether cartoon or real people) appears quite generic. Please consider submitting the banner with a few different photos in the middle for us to choose from. Ensure the image is a good fit and not simply a generic stock photo.

- Contact section: Kindly remove the phone number; we no longer wish to include it on the banner. Instead, please include our website (www.quellstaffing.com.au) and Instagram handle (@quellstaffing).

- Color scheme: White, black, and red/pink are preferred, or alternatively, blue. However, please avoid incorporating too many different colors as it may detract from the professional appearance.

We will be printing the design on a banner and require it to look professional and engaging.

Thank you once again for your submissions. I hope the feedback provided above is helpful.

Warm regards,

Target Market(s)

Allied Health Australia

Font styles to use
Serif

Colors
0054AA
0677BA
7BADD7
CADEEF
E8F1F8
0094D4
00A9DD
6FCCEA
C7EBF8
E9F6FB
EB3D1F
EC4F4E
F09395
F8D3D4
FCEDEE

```html
<!DOCTYPE html>
<html lang="en">
<head>
<meta charset="utf-8">
<title>Quell Staffing – Pull Up Banner</title>
<link href="https://fonts.googleapis.com/css2?family=Questrial&family=Montserrat:wght@700&display=swap" rel="stylesheet">
<style>
  :root {
    --brand-blue: #2c4497;
    --paper: #ffffff;
    --backdrop: #e4e6e9;
    --coat-light: #e9f3f6;
    --coat-mid: #9fc9d3;
    --shirt-teal: #3d6f7d;
  }
  * { box-sizing: border-box; margin: 0; padding: 0; }
  html, body {
    width: 846px;
    height: 1200px;
    overflow: hidden;
    background: var(--backdrop);
  }
  .banner {
    position: absolute;
    left: 171px;
    top: 20px;
    width: 503px;
    height: 1160px;
    background: var(--paper);
    overflow: hidden;
    font-family: "Questrial", sans-serif;
    color: var(--brand-blue);
  }
  .brand-name {
    position: absolute;
    left: 61px;
    top: 62px;
    font-family: "Montserrat", sans-serif;
    font-weight: 700;
    font-size: 43px;
    letter-spacing: 1px;
    line-height: 1;
    white-space: nowrap;
  }
  .headline {
    position: absolute;
    left: 58px;
    top: 158px;
    font-size: 58px;
    line-height: 61px;
    font-weight: 400;
    letter-spacing: -1px;
    white-space: nowrap;
  }
  .headline-rule {
    position: absolute;
    left: 61px;
    top: 349px;
    width: 225px;
    height: 11px;
    background: var(--brand-blue);
  }
  .specialties {
    position: absolute;
    left: 61px;
    top: 377px;
    list-style: none;
  }
  .specialties li {
    position: relative;
    padding-left: 26px;
    font-size: 45px;
    line-height: 47px;
    margin-bottom: 20px;
    white-space: nowrap;
  }
  .specialties li::before {
    content: "";
    position: absolute;
    left: 2px;
    top: 19px;
    width: 8px;
    height: 8px;
    background: var(--brand-blue);
  }
  .tagline {
    position: absolute;
    left: 61px;
    top: 666px;
    font-size: 21px;
    line-height: 26px;
    white-space: nowrap;
  }
  .illustration {
    position: absolute;
    left: 0;
    top: 0;
  }
  .contact-wave {
    position: absolute;
    left: 0;
    top: 0;
  }
  .contact {
    position: absolute;
    left: 0;
    top: 1028px;
    width: 503px;
    text-align: center;
    color: var(--paper);
  }
  .contact-title {
    font-size: 40px;
    line-height: 48px;
    font-weight: 400;
  }
  .contact-line {
    font-size: 24px;
    line-height: 29px;
    letter-spacing: 0.5px;
  }
  .contact-title + .contact-line { margin-top: 3px; }
</style>
</head>
<body>
  <main class="banner">
    <div class="brand-name">QUELL STAFFING</div>

    <h1 class="headline">HEALTHCARE<br>RECRUITMENT<br>AGENCY</h1>
    <div class="headline-rule"></div>

    <ul class="specialties">
      <li>ALLIED<br>HEALTH</li>
      <li>MEDICAL<br>IMAGING</li>
      <li>NURSING</li>
    </ul>

    <p class="tagline">Discover tailored<br>opportunities<br>based on<br>your career<br>preferences.</p>

    <svg class="illustration" width="503" height="1160" viewBox="0 0 503 1160" role="img" aria-label="Illustration of a smiling doctor in a white coat with a stethoscope, arms crossed">
      <defs>
        <linearGradient id="figure-tones" x1="0" y1="0" x2="0" y2="1">
          <stop offset="0" stop-color="var(--coat-light)"/>
          <stop offset="0.55" stop-color="var(--coat-mid)"/>
          <stop offset="1" stop-color="var(--shirt-teal)"/>
        </linearGradient>
      </defs>
      <path d="M320 470 C 320 420 360 399 400 399 C 445 399 475 430 475 475 L 475 610 C 480 640 484 650 484 660 L 484 990 L 200 990 L 200 790 C 210 730 230 700 250 690 C 280 675 300 668 318 660 L 318 600 C 312 560 312 520 320 470 Z" fill="url(#figure-tones)"/>
    </svg>

    <svg class="contact-wave" width="503" height="1160" viewBox="0 0 503 1160" aria-hidden="true">
      <path d="M0 833 C 70 950 190 1015 310 1011 C 400 1008 470 985 503 955 L 503 1160 L 0 1160 Z" fill="var(--brand-blue)"/>
    </svg>

    <section class="contact">
      <h2 class="contact-title">GET IN TOUCH:</h2>
      <p class="contact-line">WWW.QUELLSTAFFING.COM.AU</p>
      <p class="contact-line">@QUELLSTAFFING</p>
    </section>
  </main>
</body>
</html>
```